Ardoise Lumen Stationery design

With my provided logo I need stationery design for business cards, envelope (#10), letterhead, fax sheet, memo sheet and 9'' x 12'' presentation folder. I would aIso need an email signature design included. PMS COLORS are : Pantone 541C et 299C. Looking for a bold look, minimalist yet eye-catching look.

```html
<!DOCTYPE html>
<html lang="en">
<head>
<meta charset="utf-8">
<title>Ardoise Lumen – Business Card</title>
<link href="https://fonts.googleapis.com/css2?family=Montserrat:wght@500;600;700&family=Roboto:wght@400;500&display=swap" rel="stylesheet">
<style>
  :root {
    --navy: #0b4a80;
    --navy-mid: #15639a;
    --teal-blue: #1d76a6;
    --sky: #1a9ae0;
    --ink: #0f4c81;
    --grey-text: #5d6168;
    --paper: #ffffff;
    --backdrop: #232427;
  }
  * { margin: 0; padding: 0; box-sizing: border-box; }
  html, body {
    width: 1200px; height: 929px; overflow: hidden;
    background: var(--backdrop);
  }
  .canvas { position: relative; width: 1200px; height: 929px; }

  .card {
    position: absolute;
    width: 560px; height: 320px;
    border-radius: 16px;
    overflow: hidden;
    box-shadow: 0 14px 30px rgba(0,0,0,.45);
  }

  /* Front */
  .card-front {
    left: 80px; top: 90px;
    background: radial-gradient(ellipse at 65% 75%, var(--teal-blue) 0%, var(--navy-mid) 45%, var(--navy) 100%);
    display: flex; align-items: center; justify-content: center;
  }
  .brand-front {
    font-family: "Montserrat", sans-serif;
    font-weight: 600;
    font-size: 44px;
    letter-spacing: 2px;
    color: var(--paper);
    text-transform: uppercase;
  }

  /* Back */
  .card-back {
    left: 560px; top: 500px;
    background: var(--paper);
  }
  .brand-back {
    position: absolute; right: 34px; top: 34px;
    font-family: "Montserrat", sans-serif;
    font-weight: 600;
    font-size: 24px;
    letter-spacing: 1px;
    color: var(--ink);
    text-transform: uppercase;
  }
  .side-tab {
    position: absolute; left: 0; top: 118px;
    width: 18px; height: 34px;
    background: var(--ink);
    border-radius: 0 6px 6px 0;
  }
  .person { position: absolute; left: 40px; top: 112px; }
  .person-name {
    font-family: "Montserrat", sans-serif;
    font-weight: 700; font-size: 20px;
    color: var(--ink); letter-spacing: .5px;
  }
  .person-role {
    font-family: "Roboto", sans-serif;
    font-weight: 500; font-size: 16px;
    color: var(--sky); margin-top: 2px;
  }
  .address, .contacts {
    position: absolute; left: 96px;
    font-family: "Roboto", sans-serif;
    font-size: 14px; color: var(--grey-text);
    line-height: 19px;
  }
  .address { top: 186px; }
  .contacts { top: 228px; list-style: none; }
  .contacts li { display: flex; align-items: center; gap: 8px; }
  .contacts svg { width: 12px; height: 12px; fill: var(--ink); flex: none; }

  .base-band { position: absolute; left: 0; bottom: 0; width: 100%; height: 12px; display: flex; }
  .base-band .band-dark { flex: 7; background: var(--ink); }
  .base-band .band-light { flex: 3; background: var(--sky); margin-left: 2px; }
</style>
</head>
<body>
<div class="canvas">

  <section class="card card-front">
    <div class="brand-front">Ardoise Lumen</div>
  </section>

  <section class="card card-back">
    <div class="brand-back">Ardoise Lumen</div>
    <div class="side-tab"></div>

    <div class="person">
      <div class="person-name">JULIEN MARCHETTI</div>
      <div class="person-role">Director</div>
    </div>

    <div class="address">
      218 Calder Lane,<br>
      Suite 40 Westbrook, USA
    </div>

    <ul class="contacts">
      <li>
        <svg viewBox="0 0 24 24" aria-hidden="true"><path d="M6.6 10.8a15.1 15.1 0 0 0 6.6 6.6l2.2-2.2a1 1 0 0 1 1-.25 11.4 11.4 0 0 0 3.6.57 1 1 0 0 1 1 1V20a1 1 0 0 1-1 1A17 17 0 0 1 3 4a1 1 0 0 1 1-1h3.5a1 1 0 0 1 1 1c0 1.25.2 2.45.57 3.6a1 1 0 0 1-.25 1z"/></svg>
        555.204.7781
      </li>
      <li>
        <svg viewBox="0 0 24 24" aria-hidden="true"><path d="M2 5h20v14H2z M4 7v.5l8 5.5 8-5.5V7z" fill-rule="evenodd"/></svg>
        hello@ardoiselumen.com
      </li>
      <li>
        <svg viewBox="0 0 24 24" aria-hidden="true"><path d="M12 2a10 10 0 1 0 0 20 10 10 0 0 0 0-20zm0 2c1 0 2.3 2 2.8 5H9.2C9.7 6 11 4 12 4zm-3 7h6a16 16 0 0 1 0 2H9a16 16 0 0 1 0-2zm-4.9 0h3a18 18 0 0 0 0 2h-3a8 8 0 0 1 0-2zm12.8 0h3a8 8 0 0 1 0 2h-3a18 18 0 0 0 0-2zM9.2 15h5.6c-.5 3-1.8 5-2.8 5s-2.3-2-2.8-5z"/></svg>
        www.ardoiselumen.com
      </li>
    </ul>

    <div class="base-band"><span class="band-dark"></span><span class="band-light"></span></div>
  </section>

</div>
</body>
</html>
```